BrookTala UAS Business Card Design

I need a business card designed around my logo/name. I don't mind if you alter the logo slightly or have an idea to make it work different than it is. I also need a card that identifies my business by looking at the card. I am a drone operator who takes photo and video to be used for real estate listings, and mapping for construction.

Target Market(s)

Real Estate and Construction

Industry/Entity Type

Business

Contact Information for Business Card

I'd like it to be simple, but say a lot, have the "S" logo somewhere, but not doesn't have to prominent.

Font styles to use
Serif
Sans Serif

Colors
0792cd
00a990
fbed22
ffc214
f78f20
f69356
ed232b
000000
0456a4

Requirements
Must have
• "We'll get the shot you need"
• Martin Keelhaus
• Pilot / Owner
• 71 Dorrowmere Lane
• Shelton, CT 06517
• FAA 107 # 5140273
• Insured
• AeroMentor Certified
• (203) 418-5532
• brooktalauas@velmorent.com
• brooktalauas-web.com
Nice to have
• Something that hints to the client that I fly drones to take photos--I use a Korvel Aerion 4, which kind of looks like a "Y" when it is flying--I've included a few pics.
Should not have
• more than 3 colors.

```html
<!DOCTYPE html>
<html lang="en">
<head>
<meta charset="utf-8">
<title>BrookTala UAS Business Card</title>
<link rel="stylesheet" href="https://fonts.googleapis.com/css2?family=Jura:wght@700&family=Roboto:wght@400;500&display=swap">
<style>
  :root {
    --stage: #808080;
    --card: #f3f3f3;
    --edge: #d0d0d0;
    --purple: #6e60a0;
    --green: #7cc22b;
    --brand-blue: #1a5fb4;
    --ink: #3f3f3f;
    --ink-soft: #555555;
    --white: #ffffff;
  }
  * { margin: 0; padding: 0; box-sizing: border-box; }
  html, body { width: 1200px; height: 1194px; overflow: hidden; }
  body { background: var(--stage); font-family: "Roboto", Arial, sans-serif; position: relative; }

  .card {
    position: absolute; left: 264px; width: 671px; height: 404px;
    background: var(--card); border: 1px solid var(--edge); overflow: hidden;
  }
  .card--front { top: 172px; }
  .card--back { top: 618px; }

  .brand-mark {
    position: absolute; display: flex; flex-direction: column; align-items: center; gap: 18px;
  }
  .brand-mark__dot {
    border-radius: 50%; background: var(--brand-blue);
  }
  .brand-mark__name {
    font-family: "Roboto", Arial, sans-serif; font-weight: 500; color: var(--brand-blue);
    white-space: nowrap; letter-spacing: 1px;
  }
  .card--front .brand-mark { left: 0; right: 0; top: 64px; }
  .card--front .brand-mark__dot { width: 120px; height: 120px; }
  .card--front .brand-mark__name { font-size: 40px; }

  .card--back .brand-mark { left: 410px; width: 200px; top: 60px; gap: 14px; }
  .card--back .brand-mark__dot { width: 100px; height: 100px; }
  .card--back .brand-mark__name { font-size: 30px; }

  .tagline-band {
    position: absolute; left: 0; right: 0; bottom: 0; height: 44px;
    background: var(--purple); color: var(--white);
    font-size: 19px; display: flex; align-items: center; justify-content: center;
  }

  .name-accent { position: absolute; left: 0; top: 35px; width: 19px; height: 67px; background: var(--green); }
  .holder { position: absolute; left: 40px; top: 40px; }
  .holder__name { font-family: "Jura", "Arial", sans-serif; font-weight: 700; font-size: 28px; color: var(--ink); line-height: 1.1; }
  .holder__role { font-size: 16px; color: var(--ink-soft); margin-top: 2px; }

  .contact { position: absolute; left: 40px; top: 248px; list-style: none; font-size: 17px; color: var(--ink); }
  .contact li { display: flex; align-items: center; height: 24px; }
  .contact svg { width: 18px; height: 18px; margin-right: 16px; fill: var(--purple); flex: none; }
  .address { position: absolute; left: 40px; top: 325px; font-size: 17px; color: var(--ink); line-height: 26px; font-style: normal; }

  .footer-rule { position: absolute; left: 0; bottom: 0; width: 370px; height: 12px; background: var(--green); }
  .credentials {
    position: absolute; right: 0; bottom: 0; width: 318px; height: 44px;
    background: var(--purple); color: var(--white); font-size: 17px;
    clip-path: polygon(16px 0, 100% 0, 100% 100%, 0 100%);
    display: flex; align-items: center; justify-content: flex-end; padding-right: 22px; gap: 14px;
  }
</style>
</head>
<body>
  <section class="card card--front">
    <div class="brand-mark">
      <span class="brand-mark__dot"></span>
      <span class="brand-mark__name">BrookTala UAS</span>
    </div>
    <div class="tagline-band">We'll get the shot you need</div>
  </section>

  <section class="card card--back">
    <span class="name-accent"></span>
    <div class="holder">
      <h1 class="holder__name">Martin Keelhaus</h1>
      <p class="holder__role">Pilot / Owner</p>
    </div>

    <div class="brand-mark">
      <span class="brand-mark__dot"></span>
      <span class="brand-mark__name">BrookTala UAS</span>
    </div>

    <ul class="contact">
      <li><svg viewBox="0 0 24 24" aria-hidden="true"><path d="M7 1h10a2 2 0 0 1 2 2v18a2 2 0 0 1-2 2H7a2 2 0 0 1-2-2V3a2 2 0 0 1 2-2zm0 3v15h10V4H7zm5 16.2a1 1 0 1 0 0 .1z"/></svg>(203) 418-5532</li>
      <li><svg viewBox="0 0 24 24" aria-hidden="true"><path d="M3 9c0-3 4-5 9-5s9 2 9 5v2h-5V9c-1-.6-2.4-1-4-1s-3 .4-4 1v2H3V9zm3 4h12l2 8H4l2-8zm6 1.5a2.5 2.5 0 1 0 0 5 2.5 2.5 0 0 0 0-5z"/></svg>brooktalauas@velmorent.com</li>
      <li><svg viewBox="0 0 24 24" aria-hidden="true"><path d="M2 5h20v14H2V5zm2 2v.5l8 5.5 8-5.5V7H4zm0 2.9V17h16V9.9l-8 5.5-8-5.5z"/></svg>brooktalauas-web.com</li>
    </ul>

    <address class="address">71 Dorrowmere Lane Shelton,<br>CT 06517 FAA 107 # 5140273</address>

    <span class="footer-rule"></span>
    <div class="credentials"><span>Insured</span><span>|</span><span>AeroMentor Certified</span></div>
  </section>
</body>
</html>
```